KALVENTA Branded Wellness Pouch Design for Clinical Study Kit

Overview:
We are creating custom zippered pouches for our “KALVENTA Trial Spark Packs,” which will be distributed to physicians, nurses, and research coordinators participating in a national clinical study. We need a clean, professional design for the front of the pouch that incorporates our existing KALVENTA logo and the new supporting text.
Design Requirements:
Keep the existing KALVENTA logo intact (we’ll upload the file).
Add the text “Trial Spark Pack” immediately following the logo, using the same or a complementary font.
Add a tagline below that reads:
Recharge. Kalventa. Rise.
Use a layout that looks balanced, legible, and polished when printed on a small pouch.
Stay consistent with our brand color palette (blue from the logo)
The overall style should feel modern, wellness-driven, and professional — think premium, science-forward, and sleek.
Audience:
This kit will be given to medical professionals, so the design should feel elevated and credible (not flashy or overly playful).
Deliverables:
Vector file (AI, EPS)
It is a frosted white, zippered vinyl pouch (9 1/2 " x 8 1/4 " x 2 1/2 ")
The imprint size is (6 3/4" W x 4 1/2" H)
The imprint can only be 1-color, so in this case - we would like the color to be the dark blue (#06173c)

```html
<!DOCTYPE html>
<html lang="en">
<head>
<meta charset="utf-8">
<title>KALVENTA Trial Spark Pack – Pouch Imprint</title>
<link href="https://fonts.googleapis.com/css2?family=League+Spartan:wght@800&family=Oswald:wght@400;600&display=swap" rel="stylesheet">
<style>
  :root {
    --ink: #272c6a;
    --paper: #ffffff;
    --frame: #ececec;
  }
  html, body {
    margin: 0;
    padding: 0;
    width: 1200px;
    height: 1000px;
    overflow: hidden;
    background: var(--paper);
  }
  .canvas {
    position: relative;
    width: 1200px;
    height: 1000px;
  }
  .imprint-area {
    position: absolute;
    left: 113px;
    top: 185px;
    width: 974px;
    height: 649px;
    border: 1px solid var(--frame);
    box-sizing: border-box;
  }
  .lockup {
    position: absolute;
    left: 126px;
    top: 318px;
    display: flex;
    align-items: flex-start;
  }
  .brand {
    display: flex;
    flex-direction: column;
  }
  .brand-name {
    font-family: "Oswald", sans-serif;
    font-weight: 400;
    font-size: 128px;
    line-height: 1;
    letter-spacing: -1px;
    color: var(--ink);
    margin: 0;
    margin-top: -8px;
  }
  .brand-descriptor {
    font-family: "Oswald", sans-serif;
    font-weight: 400;
    font-size: 14.5px;
    line-height: 1;
    color: var(--ink);
    white-space: nowrap;
    margin-top: 2px;
  }
  .divider {
    width: 3px;
    height: 127px;
    background: var(--ink);
    margin: 8px 34px 0 34px;
  }
  .kit-name {
    font-family: "Oswald", sans-serif;
    font-weight: 600;
    font-size: 64px;
    line-height: 0.98;
    color: var(--ink);
    text-transform: uppercase;
    margin: 0;
  }
  .kit-name span { display: block; }
  .tagline {
    position: absolute;
    left: 126px;
    top: 503px;
    margin: 0;
    padding: 0;
    list-style: none;
  }
  .tagline-bar {
    height: 75px;
    background: var(--ink);
    color: var(--paper);
    font-family: "League Spartan", sans-serif;
    font-weight: 800;
    font-size: 58px;
    letter-spacing: 3px;
    line-height: 83px;
    padding-left: 42px;
    box-sizing: border-box;
    text-transform: uppercase;
  }
  .tagline-bar--short { width: 475px; }
  .tagline-bar--mid { width: 680px; margin-top: 16px; }
  .tagline-bar--long { width: 949px; margin-top: 12px; }
</style>
</head>
<body>
  <main class="canvas">
    <div class="imprint-area"></div>

    <header class="lockup">
      <div class="brand">
        <h1 class="brand-name">KALVENTA</h1>
        <div class="brand-descriptor">Lumora Disc Randomized, Sham-Controlled, Multi-Center, Double Blind Clinical Trial</div>
      </div>
      <div class="divider" aria-hidden="true"></div>
      <h2 class="kit-name"><span>Trial</span><span>Spark Pack</span></h2>
    </header>

    <ul class="tagline">
      <li class="tagline-bar tagline-bar--short">Recharge.</li>
      <li class="tagline-bar tagline-bar--mid">Kalventa.</li>
      <li class="tagline-bar tagline-bar--long">Rise.</li>
    </ul>
  </main>
</body>
</html>
```